Recruitment

Thornfield Care are now recruiting!

At Thornfield Care, we strive to provide a well-balanced community lifestyle for adults with intellectual and developmental disabilities.
We are committed to achieving high standards of care and support through the continued learning and development of the Thornfield Team.

• Family friendly company

• Competitive Pay

• Flexible working hours

• Health plan benefits

• Paid Breaks

• Full training given!

Minimum Requirements:
- A desire to make a difference to a person’s life.

We look forward to meeting you!

Please contact Dorin Velkoss on 01632 960418 at dorin.velkoss@thornfieldcare.example to arrange an interview.

(We would like the colours of the flyer to match the colours of the logo I attached - We also want the logo on the flyer)

Industry/Entity Type

Community

```html
<!DOCTYPE html>
<html lang="en">
<head>
<meta charset="utf-8">
<title>Thornfield Care – Recruitment Flyers</title>
<link href="https://fonts.googleapis.com/css2?family=Roboto+Condensed:wght@400;700&family=Roboto:wght@300;400;700&display=swap" rel="stylesheet">
<style>
  :root {
    --purple: #7a2d8b;
    --purple-dark: #652376;
    --green: #66b45c;
    --text: #555555;
    --white: #ffffff;
    --backdrop: #e6e4e1;
  }
  * { box-sizing: border-box; margin: 0; padding: 0; }
  html, body { width: 1200px; height: 875px; overflow: hidden; }
  body {
    background: var(--backdrop);
    font-family: "Roboto", Arial, sans-serif;
    color: var(--text);
    position: relative;
  }
  .flyer {
    position: absolute;
    width: 527px;
    height: 745px;
    background: var(--white);
    overflow: hidden;
    box-shadow: 0 2px 8px rgba(0,0,0,.18);
  }
  .flyer--about { left: 59px; top: 51px; }
  .flyer--benefits { left: 642px; top: 89px; }

  .flyer__header {
    position: absolute; left: 0; top: 0; width: 100%; height: 72px;
    background: var(--purple);
    color: var(--white);
    font-family: "Roboto Condensed", "Arial Narrow", sans-serif;
    font-size: 25px;
    letter-spacing: .2px;
    display: flex; align-items: center; justify-content: center;
    padding-bottom: 4px;
  }
  .flyer__band { position: absolute; left: 0; top: 0; }

  .brand {
    position: absolute; left: 0; width: 100%;
    display: flex; align-items: center; justify-content: center; gap: 10px;
  }
  .brand__dot { width: 34px; height: 34px; border-radius: 50%; background: var(--purple); }
  .brand__name {
    font-family: "Roboto Condensed", "Arial Narrow", sans-serif;
    font-size: 20px; color: var(--green); font-weight: 400;
  }

  .intro {
    position: absolute; left: 19px; right: 28px;
    font-size: 13px; line-height: 17px; font-weight: 400;
  }

  .service {
    position: absolute; top: 484px; height: 103px;
    background: var(--purple);
    color: var(--white);
    font-size: 13px; line-height: 16px; text-align: center;
    display: flex; align-items: center; justify-content: center;
  }
  .service--residential { left: 33px; width: 127px; padding-right: 8px; }
  .service--supported { left: 359px; width: 135px; }
  .service-photo { position: absolute; left: 160px; top: 456px; }

  .closing {
    position: absolute; left: 0; width: 100%; text-align: center;
    font-size: 16px; letter-spacing: .1px;
  }
  .flyer--about .closing { color: var(--purple); top: 634px; }
  .flyer--benefits .closing { color: var(--green); top: 646px; }

  .footer__contact {
    position: absolute; left: 0; width: 100%;
    color: var(--white); text-align: center;
    font-size: 11.5px; line-height: 15px;
  }
  .footer__contact strong { font-weight: 700; }
  .footer__line { display: flex; justify-content: center; align-items: center; gap: 4px; }
  .footer__line svg { flex: none; }
  .footer__gap { display: inline-block; width: 10px; }

  .benefits {
    position: absolute; left: 47px; top: 441px;
    display: grid; grid-template-columns: 249px 220px; row-gap: 15px;
    list-style: none;
  }
  .benefits li {
    display: flex; align-items: center; gap: 9px;
    font-size: 15.5px; font-weight: 300; color: var(--text); height: 20px;
  }
  .requirements {
    position: absolute; left: 42px; top: 575px;
    font-size: 14.5px; line-height: 23px;
  }
  .requirements__title { font-weight: 400; color: var(--text); }
  .requirements__item { color: var(--purple); }
</style>
</head>
<body>

<!-- About flyer -->
<section class="flyer flyer--about">
  <svg class="flyer__band" width="527" height="745" viewBox="0 0 527 745">
    <defs>
      <linearGradient id="houseTones" x1="0" y1="0" x2="1" y2="1">
        <stop offset="0" stop-color="#9cc0dc"/>
        <stop offset=".4" stop-color="#b0603f"/>
        <stop offset=".75" stop-color="#5d7a3a"/>
        <stop offset="1" stop-color="#3f5a2a"/>
      </linearGradient>
    </defs>
    <path role="img" aria-label="Photo of a red-brick care home with a garden" d="M0 66 Q263 78 527 70 V240 Q260 236 0 256 Z" fill="url(#houseTones)"/>
    <path d="M0 0 H527 V70 Q263 76 0 66 Z" fill="var(--purple)"/>
    <path d="M0 684 Q263 662 527 676 V745 H0 Z" fill="var(--green)"/>
  </svg>
  <h1 class="flyer__header">THORNFIELD CARE ARE NOW RECRUITING!</h1>

  <div class="brand" style="top:282px">
    <span class="brand__dot"></span>
    <span class="brand__name">THORNFIELD CARE</span>
  </div>

  <p class="intro" style="top:353px">At Thornfield Care, we strive to provide a well-balanced community lifestyle for adults with intellectual and developmental disabilities.</p>
  <p class="intro" style="top:402px">We are committed to achieving high standards of care and support through the continued learning and development of the Thornfield Team.</p>

  <div class="service service--residential">RESIDENTIAL<br>CARE</div>
  <svg class="service-photo" width="199" height="172" viewBox="0 0 199 172">
    <defs>
      <linearGradient id="carerTones" x1="0" y1="0" x2="1" y2="1">
        <stop offset="0" stop-color="#dfe6ea"/>
        <stop offset=".45" stop-color="#8fb6d6"/>
        <stop offset="1" stop-color="#5d6f8c"/>
      </linearGradient>
    </defs>
    <path role="img" aria-label="Photo of a carer reviewing a folder with a resident" d="M0 0 H199 V164 H103 L99 172 L95 164 H0 Z" fill="url(#carerTones)"/>
  </svg>
  <div class="service service--supported">SUPPORTED<br>LIVING</div>

  <p class="closing">WE LOOK FORWARD TO MEETING YOU!</p>

  <div class="footer__contact" style="top:690px">
    <p>Please contact <strong>Dorin Velkoss</strong></p>
    <p class="footer__line">
      <svg width="11" height="11" viewBox="0 0 12 12"><circle cx="6" cy="6" r="6" fill="#fff"/><path d="M4 3 L5.2 4.6 L4.6 5.4 Q5.4 7 6.8 7.6 L7.6 7 L9 8.2 L8.3 9.2 Q5.5 9 3.2 5.2 Q3.3 3.6 4 3 Z" fill="var(--green)"/></svg>
      01632 960418<span class="footer__gap"></span>
      <svg width="11" height="11" viewBox="0 0 12 12"><circle cx="6" cy="6" r="6" fill="#fff"/><rect x="3" y="4" width="6" height="4.2" fill="none" stroke="var(--green)" stroke-width=".9"/><path d="M3 4 L6 6.4 L9 4" fill="none" stroke="var(--green)" stroke-width=".9"/></svg>
      dorin.velkoss@thornfieldcare.example
    </p>
    <p>to arrange an interview.</p>
  </div>
</section>

<!-- Benefits flyer -->
<section class="flyer flyer--benefits">
  <svg class="flyer__band" width="527" height="745" viewBox="0 0 527 745">
    <defs>
      <linearGradient id="bedroomTones" x1="0" y1="0" x2="1" y2="1">
        <stop offset="0" stop-color="#d8c8b2"/>
        <stop offset=".5" stop-color="#9c8470"/>
        <stop offset=".8" stop-color="#c98a6a"/>
        <stop offset="1" stop-color="#e7a3b5"/>
      </linearGradient>
    </defs>
    <path role="img" aria-label="Photo of a support worker reading with a resident in a bedroom" d="M0 70 Q263 82 527 72 V335 Q260 322 0 348 Z" fill="url(#bedroomTones)"/>
    <path d="M0 0 H527 V72 Q263 80 0 70 Z" fill="var(--purple)"/>
    <path d="M0 693 Q263 668 527 682 V745 H0 Z" fill="var(--green)"/>
  </svg>
  <h1 class="flyer__header" style="height:75px">THORNFIELD CARE ARE NOW RECRUITING!</h1>

  <div class="brand" style="top:368px">
    <span class="brand__dot"></span>
    <span class="brand__name">THORNFIELD CARE</span>
  </div>

  <ul class="benefits">
    <li><svg width="20" height="20" viewBox="0 0 20 20"><circle cx="10" cy="10" r="10" fill="var(--purple)"/><path d="M8 5.5 L12.5 10 L8 14.5" fill="none" stroke="#fff" stroke-width="2.2"/></svg>Family friendly company</li>
    <li><svg width="20" height="20" viewBox="0 0 20 20"><circle cx="10" cy="10" r="10" fill="var(--purple)"/><path d="M8 5.5 L12.5 10 L8 14.5" fill="none" stroke="#fff" stroke-width="2.2"/></svg>Health plan benefits</li>
    <li><svg width="20" height="20" viewBox="0 0 20 20"><circle cx="10" cy="10" r="10" fill="var(--purple)"/><path d="M8 5.5 L12.5 10 L8 14.5" fill="none" stroke="#fff" stroke-width="2.2"/></svg>Competitive Pay</li>
    <li><svg width="20" height="20" viewBox="0 0 20 20"><circle cx="10" cy="10" r="10" fill="var(--purple)"/><path d="M8 5.5 L12.5 10 L8 14.5" fill="none" stroke="#fff" stroke-width="2.2"/></svg>Paid Breaks</li>
    <li><svg width="20" height="20" viewBox="0 0 20 20"><circle cx="10" cy="10" r="10" fill="var(--purple)"/><path d="M8 5.5 L12.5 10 L8 14.5" fill="none" stroke="#fff" stroke-width="2.2"/></svg>Flexible working hours</li>
    <li><svg width="20" height="20" viewBox="0 0 20 20"><circle cx="10" cy="10" r="10" fill="var(--purple)"/><path d="M8 5.5 L12.5 10 L8 14.5" fill="none" stroke="#fff" stroke-width="2.2"/></svg>Full training given!</li>
  </ul>

  <div class="requirements">
    <p class="requirements__title">Minimum Requirements:</p>
    <p class="requirements__item">- A desire to make a difference to a persons life.</p>
  </div>

  <p class="closing">WE LOOK FORWARD TO MEETING YOU!</p>

  <div class="footer__contact" style="top:683px">
    <p>Please contact <strong>Dorin Velkoss</strong></p>
    <p class="footer__line">
      <svg width="11" height="11" viewBox="0 0 12 12"><circle cx="6" cy="6" r="6" fill="#fff"/><path d="M4 3 L5.2 4.6 L4.6 5.4 Q5.4 7 6.8 7.6 L7.6 7 L9 8.2 L8.3 9.2 Q5.5 9 3.2 5.2 Q3.3 3.6 4 3 Z" fill="var(--green)"/></svg>
      01632 960418<span class="footer__gap"></span>
      <svg width="11" height="11" viewBox="0 0 12 12"><circle cx="6" cy="6" r="6" fill="#fff"/><rect x="3" y="4" width="6" height="4.2" fill="none" stroke="var(--green)" stroke-width=".9"/><path d="M3 4 L6 6.4 L9 4" fill="none" stroke="var(--green)" stroke-width=".9"/></svg>
      dorin.velkoss@thornfieldcare.example
    </p>
    <p>to arrange an interview.</p>
  </div>
</section>

</body>
</html>
```